【 概要 】 野球系CLIPVEXのサムネイル案を募集いたします。 【 依頼内容 】 ・テーマ:森川健吾 『2021年殊勲打のホームラン集』 かっこいい森川健吾選手の画像を使ってください。 ・ 解像度1280×720(最小幅640ピクセル) ・作成数: 1種類 ・Photoshopで作成。 プロジェクトファイルの納品をお願い致します。 文字はテキストレイヤーのままでお願い致します。 【 デザインイメージ 】 ・参考デザイン: https://www.clipvex.example/c/KAZEBATTERClips 【 契約金額(税込) 】 1案 ¥1500 ※契約金額(税込)からシステム利用料を差し引いた金額が、ワーカーさまの受取金額となります その他ご質問等ありましたら、気軽にお問い合わせください。 ご応募をお待ちしております! |
| https://www.clipvex.example/c/KAZEBATTERClips | ||
こちらが一番イメージに近かったためです。
皆様ご提案どうもありがとうございました。
また機会がございましたら宜しくお願い致します。

```html
<!DOCTYPE html>
<html lang="ja">
<head>
<meta charset="utf-8">
<title>森川健吾 2021年 珠勲打のホームラン集</title>
<link href="https://fonts.googleapis.com/css2?family=Noto+Sans+JP:wght@900&display=swap" rel="stylesheet">
<style>
  :root {
    --title-red: #e8141c;
    --title-blue: #1d3fd8;
    --outline-white: #ffffff;
    --gold-light: #f3e3b0;
    --gold-mid: #c9a55a;
    --gold-dark: #7d6128;
    --stadium-dark: #1f2430;
    --stadium-mid: #4a505c;
    --jersey-light: #e9e6e4;
    --helmet-red: #c8202a;
  }
  html, body {
    margin: 0;
    padding: 0;
    width: 1200px;
    height: 676px;
    overflow: hidden;
    background: var(--stadium-dark);
  }
  .thumbnail {
    position: relative;
    width: 1200px;
    height: 676px;
    overflow: hidden;
    font-family: "Noto Sans JP", sans-serif;
  }
  .player-photo {
    position: absolute;
    inset: 0;
    background:
      radial-gradient(ellipse 210px 150px at 960px 80px, var(--helmet-red) 0%, rgba(200,32,42,0) 70%),
      radial-gradient(ellipse 300px 380px at 900px 420px, var(--jersey-light) 0%, rgba(233,230,228,0.5) 55%, rgba(233,230,228,0) 80%),
      linear-gradient(100deg, var(--stadium-dark) 0%, var(--stadium-mid) 45%, #6b6f78 70%, var(--stadium-dark) 100%);
  }
  .headline {
    position: absolute;
    inset: 0;
    width: 1200px;
    height: 676px;
  }
  .headline text {
    font-family: "Noto Sans JP", sans-serif;
    font-weight: 900;
    paint-order: stroke fill;
    stroke-linejoin: round;
  }
  .player-name { fill: var(--title-red); stroke: var(--outline-white); stroke-width: 14px; }
  .season { fill: var(--title-red); stroke: var(--outline-white); stroke-width: 12px; }
  .feat-word { fill: url(#goldFill); stroke: var(--outline-white); stroke-width: 12px; }
  .particle { fill: var(--title-red); stroke: var(--outline-white); stroke-width: 12px; }
  .collection { fill: var(--title-blue); stroke: var(--outline-white); stroke-width: 16px; }
</style>
</head>
<body>
  <div class="thumbnail">
    <div class="player-photo" role="img" aria-label="スタジアムを背景に、赤いヘルメットと白いユニフォームでバットを振り抜く森川健吾選手の写真"></div>
    <svg class="headline" viewBox="0 0 1200 676" xmlns="http://www.w3.org/2000/svg" aria-label="森川健吾 2021年 珠勲打のホームラン集">
      <defs>
        <linearGradient id="goldFill" x1="0" y1="0" x2="0" y2="1">
          <stop offset="0" stop-color="var(--gold-light)"/>
          <stop offset="0.5" stop-color="var(--gold-mid)"/>
          <stop offset="1" stop-color="var(--gold-dark)"/>
        </linearGradient>
      </defs>
      <text class="player-name" x="18" y="192" font-size="128" textLength="512" lengthAdjust="spacingAndGlyphs">森川健吾</text>
      <text class="season" x="14" y="396" font-size="124" textLength="524" lengthAdjust="spacingAndGlyphs">2021年</text>
      <text class="feat-word" x="540" y="420" font-size="176" textLength="540" lengthAdjust="spacingAndGlyphs">珠勲打</text>
      <text class="particle" x="1086" y="400" font-size="118">の</text>
      <text class="collection" x="10" y="628" font-size="196" textLength="1020" lengthAdjust="spacingAndGlyphs">ホームラン</text>
      <text class="collection" x="1050" y="624" font-size="128">集</text>
    </svg>
  </div>
</body>
</html>
```